Business Cards for our company

Hi there,

we have successfully designed a logo with ArtFlock and would like now to design our business cards. We would like to keep the colours and the look-and-feel of the logo. Please send in variations with two or three colours and one or two sides. I promise to respond to every single submission.

Many thanks and happy new year.

All the best,
Wilfried

Target Market(s)

B2B

Industry/Entity Type

Trade

Contact Information for Business Card

We have successfully designed a logo with ArtFlock and would like now to design our business cards. We would like to keep the colours and the look-and-feel of the logo. Please send in variations with two or three colours and one or two sides. I promise to respond to every single submission.

Font styles to use
Serif
Sans Serif
Script

Requirements
Must have
• These information should be on the business card, grouped as you suggest, and we think using small pictograms for mobile, email, etc is pretty helpful:
• Wilfried Tammler (first and second name)
• Geschäftsführer/ Managing Director (title)
• KoR Warenkontor GmbH (company name and legal form)
• Ostheimer Str. 18/3 (street and house number)
• 71254 Altbrunn (zip code and town)
• +491709384562 (mobile)
• +4972419027341 (work)
• w.tammler@kor-warenkontor.example (email)
• www.kor-warenkontor.example (web)
Nice to have
• Spectacular and interesting layout and design. You look at it and think, wow, that's not the normal stuff.
• We think of ourselves as bridge-builders between businesses (international producers on the one hand, and retail chains on the other hand) and we translate, organise and manage projects where both partners are involved, but it's difficult for them to cooperate due to language barriers and different working cultures.
• This is why we have the n between the B's shaped as a bridge, and the green arc supports this idea. Maybe you could play with this idea...
Should not have
• the standard layout that everybody has

```html
<!DOCTYPE html>
<html lang="en">
<head>
<meta charset="utf-8">
<title>Warenkontor – Business Card</title>
<link rel="stylesheet" href="https://fonts.googleapis.com/css2?family=Montserrat:wght@400;700&display=swap">
<style>
  :root {
    --page: #2b2e2d;
    --card: #0d0d0d;
    --card-sheen: #262626;
    --green: #9ccc2e;
    --white: #f2f2f2;
    --grey: #b8b8b8;
    --panel: #f4f4f4;
    --logo-ink: #2a2a2a;
  }
  * { margin: 0; padding: 0; box-sizing: border-box; }
  html, body {
    width: 1200px;
    height: 900px;
    overflow: hidden;
    background: var(--page);
    font-family: "Montserrat", Arial, sans-serif;
  }
  .card {
    position: absolute;
    left: 100px;
    top: 164px;
    width: 1000px;
    height: 572px;
    background:
      radial-gradient(ellipse at 35% 40%, var(--card-sheen) 0%, var(--card) 65%),
      var(--card);
    overflow: hidden;
    box-shadow: 0 20px 50px rgba(0,0,0,0.5);
  }
  .logo-band {
    position: absolute;
    top: 34px;
    right: 0;
    width: 480px;
    height: 108px;
  }
  .logo-band svg { position: absolute; inset: 0; }
  .brand-name {
    position: absolute;
    left: 90px;
    right: 30px;
    top: 0;
    height: 92px;
    display: flex;
    align-items: center;
    justify-content: center;
    font-size: 38px;
    font-weight: 700;
    color: var(--logo-ink);
    letter-spacing: 1px;
  }
  .contact {
    position: absolute;
    right: 50px;
    top: 172px;
    text-align: right;
    color: var(--white);
    font-size: 21px;
    line-height: 1.3;
  }
  .label {
    color: var(--green);
    font-weight: 700;
    font-size: 19px;
    letter-spacing: 0.5px;
    text-transform: uppercase;
  }
  .contact .label + p { margin-top: 2px; }
  .contact .group + .group { margin-top: 26px; }
  .identity {
    position: absolute;
    left: 120px;
    top: 320px;
  }
  .person-name {
    color: var(--green);
    font-weight: 700;
    font-size: 30px;
    letter-spacing: 0.5px;
    text-transform: uppercase;
  }
  .person-title {
    color: var(--grey);
    font-size: 20px;
    letter-spacing: 1px;
    text-transform: uppercase;
  }
  .address {
    position: absolute;
    left: 162px;
    top: 418px;
    color: var(--white);
    font-size: 22px;
    line-height: 1.3;
  }
  .address .label { font-size: 21px; margin-bottom: 4px; }
</style>
</head>
<body>
  <section class="card" aria-label="Business card, KoR Warenkontor GmbH">
    <div class="logo-band">
      <svg width="480" height="108" viewBox="0 0 480 108" aria-hidden="true">
        <polygon points="60,0 480,0 480,92 0,92" fill="var(--panel)"/>
        <polygon points="0,94 480,94 480,104 6,104" fill="var(--green)"/>
      </svg>
      <div class="brand-name">WARENKONTOR</div>
    </div>

    <div class="contact">
      <div class="group">
        <p class="label">Phone &amp; Mobile</p>
        <p>+491709384562</p>
        <p>+4972419027341</p>
      </div>
      <div class="group">
        <p class="label">Web &amp; Email</p>
        <p>w.tammler@kor-warenkontor.example</p>
        <p>www.kor-warenkontor.example</p>
      </div>
    </div>

    <div class="identity">
      <h1 class="person-name">Wilfried Tammler</h1>
      <p class="person-title">Managing Director</p>
    </div>

    <div class="address">
      <p class="label">Addrees</p>
      <p>18/3.Ostheimer Str.</p>
      <p>71254 Altbrunn</p>
    </div>
  </section>
</body>
</html>
```